Bright Oak Consultant Services

I'm looking to create a flyer for my business to provide a consultant service. I will be providing the following below
Launch Your Business Today for only $150
(state fee not included)
Business Formation includes:
*Limited liability Corporation (LLC)
*Hale and Penwick Number
*FEIN
*Operation Agreement for partnership LLCs (For 2 or more member(s)
*Commercial Activity license (If needed for your Business )
*Same -day turnaround service with documents
Schedule your Appointment today
Call or text:413-902-6175
Email:MorvellCapitalCircle@quillpost.net
Target Market(s)
I want the flyer to attract people who wants to start a business but doesn’t know where to start. I want the flyer to stand out form the other consultant businesses.
Industry/Entity Type
Consultant
Requirements
Must have
- The State fee not included should be in small print
Highlight the price or service
Highlight the phrase "launch you business today"
Nice to have
- Different samples of colors, a variety
Should not have
- should not be all one color

```html
<!DOCTYPE html>
<html lang="en">
<head>
<meta charset="utf-8">
<title>Bright Oak Consultant Services – Business Formation Flyer</title>
<link rel="stylesheet" href="https://fonts.googleapis.com/css2?family=Archivo:wght@500;600&family=Montserrat:wght@400;500;700;900&family=Roboto+Condensed:wght@700&display=swap">
<style>
  :root {
    --navy: #123a8a;
    --royal: #1a4fb0;
    --sky: #2f7fd3;
    --ink-navy: #0d2451;
    --check: #2a6cc6;
    --title-blue: #1d58b8;
    --text: #1d1d1f;
    --white: #ffffff;
    --backdrop: #e9ebef;
  }
  * { margin: 0; padding: 0; box-sizing: border-box; }
  html, body { width: 1200px; height: 1200px; overflow: hidden; background: var(--backdrop); }
  .flyer {
    position: absolute; left: 160px; top: 30px;
    width: 880px; height: 1140px;
    background: var(--white); overflow: hidden;
    box-shadow: 0 6px 24px rgba(0,0,0,.18);
  }
  .header-shape { position: absolute; left: 0; top: 0; width: 880px; height: 470px; }
  .headline {
    position: absolute; left: 0; top: 100px; width: 880px;
    text-align: center; color: var(--white);
  }
  .headline-line {
    display: block; font-family: "Archivo", Arial, sans-serif;
    font-weight: 600; font-size: 66px; line-height: 1.02; letter-spacing: 0.5px;
  }
  .headline-price {
    display: block; font-family: "Montserrat", Arial, sans-serif;
    font-weight: 900; font-size: 112px; line-height: 1.0; margin-top: 4px;
  }
  .fine-print {
    position: absolute; left: 575px; top: 372px;
    font-family: "Montserrat", Arial, sans-serif; font-size: 13px; color: var(--white);
  }
  .includes { position: absolute; left: 0; top: 500px; width: 880px; }
  .includes-frame { position: absolute; left: 80px; top: 0; width: 720px; height: 60px; }
  .includes-title {
    position: absolute; left: 0; width: 880px; top: 10px; text-align: center;
    font-family: "Roboto Condensed", Arial, sans-serif; font-weight: 700;
    font-size: 32px; color: var(--title-blue); letter-spacing: .3px;
  }
  .feature-grid {
    position: absolute; left: 90px; top: 590px; width: 700px;
    list-style: none;
    display: grid; grid-template-columns: repeat(3, 1fr); row-gap: 44px;
  }
  .feature { list-style: none; text-align: center; font-family: "Montserrat", Arial, sans-serif; font-size: 16.5px; line-height: 1.25; color: var(--text); }
  .feature-check { display: block; margin: 0 auto 12px; width: 66px; height: 56px; }
  .footer {
    position: absolute; left: 0; top: 950px; width: 880px; height: 190px;
    background: linear-gradient(90deg, var(--navy), var(--royal) 60%, var(--navy));
  }
  .appointment-tag {
    position: absolute; left: 155px; top: 925px;
    background: var(--ink-navy); color: var(--white);
    font-family: "Roboto Condensed", Arial, sans-serif; font-weight: 700;
    font-size: 30px; padding: 6px 18px; letter-spacing: .3px;
  }
  .call-line {
    position: absolute; left: 0; top: 1010px; width: 880px; text-align: center;
    color: var(--white); font-family: "Montserrat", Arial, sans-serif;
  }
  .call-label { font-weight: 400; font-size: 40px; letter-spacing: 2px; }
  .call-number { font-weight: 700; font-size: 42px; margin-left: 8px; }
  .email-line {
    position: absolute; left: 0; top: 1075px; width: 880px; text-align: center;
    color: var(--white); font-family: "Montserrat", Arial, sans-serif; font-size: 16px;
  }
</style>
</head>
<body>
<main class="flyer">
  <svg class="header-shape" viewBox="0 0 880 470" aria-hidden="true">
    <defs>
      <linearGradient id="headerGrad" x1="0" y1="0" x2="1" y2="1">
        <stop offset="0" stop-color="#1c4aa6"/>
        <stop offset="1" stop-color="#13398a"/>
      </linearGradient>
    </defs>
    <polygon points="0,0 880,0 880,375 470,465 0,440" fill="#153f92"/>
    <polygon points="0,355 470,465 0,440" fill="var(--sky)"/>
    <polygon points="0,0 880,0 880,375 470,465 0,355" fill="url(#headerGrad)" role="img" aria-label="Faded photo of a desk with documents and a pen, tinted blue"/>
  </svg>

  <h1 class="headline">
    <span class="headline-line">LAUNCH YOUR</span>
    <span class="headline-line">BUSINESS TODAY FOR</span>
    <span class="headline-price">ONLY $150</span>
  </h1>
  <p class="fine-print">(state fee not included)</p>

  <section class="includes">
    <svg class="includes-frame" viewBox="0 0 720 60" aria-hidden="true">
      <polyline points="0,58 0,32 120,32" fill="none" stroke="var(--title-blue)" stroke-width="2"/>
      <polyline points="600,32 720,32 720,58" fill="none" stroke="var(--title-blue)" stroke-width="2"/>
    </svg>
    <h2 class="includes-title">BUSINESS FORMATION INCLUDES:</h2>
  </section>

  <ul class="feature-grid">
    <li class="feature">
      <svg class="feature-check" viewBox="0 0 66 56" aria-hidden="true"><path d="M44 6H4v46h46V32" fill="none" stroke="var(--check)" stroke-width="7"/><path d="M18 24l12 12 30-30" fill="none" stroke="var(--check)" stroke-width="6"/></svg>
      Limited liability<br>Corporation (LLC)
    </li>
    <li class="feature">
      <svg class="feature-check" viewBox="0 0 66 56" aria-hidden="true"><path d="M44 6H4v46h46V32" fill="none" stroke="var(--check)" stroke-width="7"/><path d="M18 24l12 12 30-30" fill="none" stroke="var(--check)" stroke-width="6"/></svg>
      Hale and Penwick<br>Number
    </li>
    <li class="feature">
      <svg class="feature-check" viewBox="0 0 66 56" aria-hidden="true"><path d="M44 6H4v46h46V32" fill="none" stroke="var(--check)" stroke-width="7"/><path d="M18 24l12 12 30-30" fill="none" stroke="var(--check)" stroke-width="6"/></svg>
      FEIN
    </li>
    <li class="feature">
      <svg class="feature-check" viewBox="0 0 66 56" aria-hidden="true"><path d="M44 6H4v46h46V32" fill="none" stroke="var(--check)" stroke-width="7"/><path d="M18 24l12 12 30-30" fill="none" stroke="var(--check)" stroke-width="6"/></svg>
      Operation Agreement for<br>partnership LLCs (For 2 or<br>more member(s)
    </li>
    <li class="feature">
      <svg class="feature-check" viewBox="0 0 66 56" aria-hidden="true"><path d="M44 6H4v46h46V32" fill="none" stroke="var(--check)" stroke-width="7"/><path d="M18 24l12 12 30-30" fill="none" stroke="var(--check)" stroke-width="6"/></svg>
      Commercial Activity<br>license (If needed for<br>your Business )
    </li>
    <li class="feature">
      <svg class="feature-check" viewBox="0 0 66 56" aria-hidden="true"><path d="M44 6H4v46h46V32" fill="none" stroke="var(--check)" stroke-width="7"/><path d="M18 24l12 12 30-30" fill="none" stroke="var(--check)" stroke-width="6"/></svg>
      Same -day<br>turnaround service<br>with documents
    </li>
  </ul>

  <footer class="footer"></footer>
  <p class="appointment-tag">SCHEDULE YOUR APPOINTMENT TODAY</p>
  <p class="call-line"><span class="call-label">CALL OR TEXT</span><span class="call-number">413-902-6175</span></p>
  <p class="email-line">Email : MorvellCapitalCircle@quillpost.net</p>
</main>
</body>
</html>
```